Exclusive Pet groomer Post Card

We need a design for a direct mailing postcard. We want to include images of some of dogs and cats done the list of our services and the benefits of our company.

I like something like: Does your pet look like any of these or is a similar breed?

If your answer is yes, then it deserves the best groomer in town

any ideas are welcome!

URGENT Mailing Postcard needed!

Elegant, modern and clean sophisticated card that has images of the dogs and cats provided. I will use the original images from the image bank once the project is approved. As a designer you just need to create the layout for this and the organization!

Thanks

Target Market(s)

High Income professionals that will pay for premium services for their pets.

Industry/Entity Type

Pet

Requirements
Must have
• A full color double sided postcard. 5.5 x 8.5 in postcard. (I want to have all pics uploaded. I used some sample images from stock photo but once approved I will purchase the images at the respective site). Must have space to place recipient address and space for NPDS stamp. ( is a postcard to be mailed!)

I would like to have the following text in the post card:

Enhance the beauty of your pets
Pamper your best friend
Give to your dog or cat the stylish treatment it deserves

One of the top groomers in town
Experienced in dogs and cats
Clean individual pet grooming stations (Sanitation and Sterilization)
Services:
Full service grooming* services for dogs and cats include:
Day Spa, High Fashion Haircuts, hair trimming, nail clipping and “Petticures”
Bathing, gentle ear Cleaning, sanitary trim, Brushing, Fluff Drying and Dematting
* Regular grooming ensures happier and healthier pets

Fur Harbor Trim
2716 NE 147th Street, North Miami, Florida 33181
T. 305-647-3918
www.furharbortrim.example
Nice to have
• Logo as in the website

```html
<!DOCTYPE html>
<html lang="en">
<head>
<meta charset="utf-8">
<title>Fur Harbor Trim – Grooming Postcard</title>
<link rel="stylesheet" href="https://fonts.googleapis.com/css2?family=Montserrat:ital,wght@0,400;0,500;0,800;0,900;1,700;1,800&family=Arimo:wght@400&display=swap">
<style>
  :root {
    --stage: #3b3b3b;
    --card: #ffffff;
    --magenta: #e5007e;
    --sky: #1a9ae0;
    --blue-copy: #1e8fe6;
    --ink: #2b2b2b;
    --purple: #5a2c8c;
    --rule: #9a9a9a;
    --line: #b8b8b8;
    --stamp-zone: #f1efec;
    --stamp: #7b5aa8;
    --fur-dark: #6b4a2e;
    --fur-light: #c9a07a;
    --cat: #c98f55;
  }
  * { box-sizing: border-box; margin: 0; padding: 0; }
  html, body { width: 1200px; height: 596px; overflow: hidden; background: var(--stage); }
  .stage { position: relative; width: 1200px; height: 596px; }
  .card {
    position: absolute; top: 52px; width: 528px; height: 342px;
    background: var(--card); overflow: hidden;
    font-family: "Arimo", Arial, sans-serif; color: var(--ink);
  }
  .card--front { left: 44px; }
  .card--back { left: 628px; }
  .card svg.band { position: absolute; left: 0; top: 0; }

  .headline {
    position: absolute; font-family: "Montserrat", Arial, sans-serif; font-weight: 900;
    line-height: 1.08;
  }
  .card--front .headline {
    left: 19px; top: 14px; font-size: 19.5px; color: #fff;
    text-shadow: 1px 2px 3px rgba(0,0,0,.35);
    transform: rotate(-1.5deg); transform-origin: left top;
  }
  .card--back .headline {
    left: 22px; top: 46px; font-size: 15.5px; color: var(--magenta);
    line-height: 1.18; text-shadow: 1px 2px 3px rgba(0,0,0,.3);
  }

  .benefits {
    position: absolute; left: 16px; top: 134px;
    font-family: "Montserrat", Arial, sans-serif; font-style: italic; font-weight: 800;
    font-size: 11.6px; line-height: 1.12; color: var(--blue-copy);
  }
  .services { position: absolute; font-size: 7.6px; line-height: 1.45; color: var(--ink); }
  .services h3 { font-weight: 400; font-size: 10.5px; line-height: 1.2; }
  .card--front .services { left: 16px; top: 200px; }
  .card--back .services { left: 22px; top: 138px; }

  .photo { position: absolute; }
  .photo--dog {
    right: 0; top: 104px; width: 268px; height: 238px;
    background: radial-gradient(ellipse 60% 60% at 55% 55%, var(--fur-dark) 0%, var(--fur-light) 55%, rgba(255,255,255,0) 100%);
  }
  .photo--cat {
    left: 106px; top: 192px; width: 160px; height: 86px;
    background: radial-gradient(ellipse 55% 50% at 50% 55%, var(--cat) 0%, #e3bf98 60%, rgba(255,255,255,0) 100%);
  }

  .signoff { position: absolute; display: flex; align-items: center; }
  .card--front .signoff { left: 16px; top: 288px; }
  .card--back .signoff { left: 18px; top: 288px; }
  .brand { display: flex; align-items: center; gap: 5px; width: 120px; }
  .brand-mark { width: 9px; height: 9px; background: var(--purple); }
  .brand-name {
    font-family: "Montserrat", Arial, sans-serif; font-weight: 800; font-size: 11.5px;
    color: var(--purple); white-space: nowrap;
  }
  .contact { border-left: 1px solid var(--rule); padding-left: 6px; margin-left: 4px; }
  .contact .address { font-size: 8.6px; line-height: 1.2; }
  .contact .phone { font-family: "Montserrat", Arial, sans-serif; font-weight: 500; font-size: 13.5px; line-height: 1.2; }
  .contact .web { font-size: 8.6px; }
  .contact .web b { color: var(--magenta); font-weight: 400; }

  .stamp-zone {
    position: absolute; left: 362px; top: 13px; width: 138px; height: 85px;
    background: var(--stamp-zone);
  }
  .stamp {
    position: absolute; right: 11px; top: 9px; width: 46px; height: 60px;
    background: var(--stamp);
  }
  .address-lines { position: absolute; left: 288px; top: 161px; width: 202px; }
  .address-lines span { display: block; height: 24px; border-bottom: 1px solid var(--line); }
</style>
</head>
<body>
<main class="stage">

  <article class="card card--front">
    <svg class="band" width="528" height="130" viewBox="0 0 528 130" aria-hidden="true">
      <polygon points="0,0 528,0 528,96 0,121" fill="var(--magenta)"/>
      <polygon points="0,121 528,96 528,101 0,126" fill="var(--sky)"/>
    </svg>
    <div class="photo photo--dog" role="img" aria-label="Photo of a groomed Yorkshire terrier with a pink bow, lying down"></div>
    <h1 class="headline">Enhance the beauty of your pets<br>Pamper your best friend<br>Give to your dog or cat<br>the stylish treatment it deserves</h1>
    <p class="benefits">One of the top groomers in town,<br>Experienced in dogs and cats<br>Clean individual pet grooming stations<br>(Sanitation and Sterilization)</p>
    <section class="services">
      <h3>Services:</h3>
      <p>Full service grooming* services for dogs and cats include:<br>Day Spa, High Fashion Haircuts, hair trimming, nail clipping and “Petticures”<br>Bathing, gentle ear Cleaning, sanitary trim, Brushing, Fluff Drying and Dematting<br>* Regular grooming ensures happier and healthier pets</p>
    </section>
    <footer class="signoff">
      <div class="brand"><span class="brand-mark"></span><span class="brand-name">Fur Harbor Trim</span></div>
      <div class="contact">
        <p class="address">2716 NE 147th Street,<br>North Miami, Florida 33181</p>
        <p class="phone">Call 305-647-3918</p>
        <p class="web">www.<b>furharbortrim</b>.example</p>
      </div>
    </footer>
  </article>

  <article class="card card--back">
    <svg class="band" width="528" height="60" viewBox="0 0 528 60" aria-hidden="true">
      <polygon points="0,0 340,0 0,42" fill="var(--magenta)"/>
      <polygon points="0,42 340,0 355,0 0,47" fill="var(--sky)"/>
    </svg>
    <div class="stamp-zone" aria-label="Postage area">
      <div class="stamp" role="img" aria-label="Postage stamp"></div>
    </div>
    <h1 class="headline">Enhance the beauty of your pets<br>Pamper your best friend<br>Give to your dog or cat the stylish<br>treatment it deserves</h1>
    <section class="services">
      <h3>Services:</h3>
      <p>Full service grooming* services for dogs and cats include:<br>Day Spa, High Fashion Haircuts, hair trimming, nail clipping and “Petticures”<br>Bathing, gentle ear Cleaning, sanitary trim, Brushing, Fluff Drying and Dematting<br>* Regular grooming ensures happier and healthier pets</p>
    </section>
    <div class="photo photo--cat" role="img" aria-label="Photo of a long-haired ginger Persian cat"></div>
    <div class="address-lines" aria-label="Recipient address"><span></span><span></span><span></span><span></span><span></span></div>
    <footer class="signoff">
      <div class="brand"><span class="brand-mark"></span><span class="brand-name">Fur Harbor Trim</span></div>
      <div class="contact">
        <p class="address">2716 NE 147th Street,<br>North Miami, Florida 33181</p>
        <p class="phone">Call 305-647-3918</p>
        <p class="web">www.<b>furharbortrim</b>.example</p>
      </div>
    </footer>
  </article>

</main>
</body>
</html>
```